Business Card and Letterhead Design Project

I am starting my own building design business in Melbourne. The business will use my experience to help people make balanced life choices for building and renovating. My target audience is women -particularly mothers. I aim to be approachable and economical. I would like to see a design that uses greens or blues - natural colours. A lot of my work balances design and construction management so design should be flexible.

I want a double sided business card design and a letterhead design that I can use on all office correspondance

Design should have a clean crisp feel - a bit edgey in a feminine way.

Target Market(s)

Potential clients.

Industry/Entity Type

Construction

Requirements
Must have
• Brackenridge Design Studio
Harriet Oakley B.Arch

0497 283 541
harriet@brackenridgedesignstudio.example.au

14 Pembury Road
Kilmarra Heights VIC 3187
brackenridgedesignstudio.example.au
Nice to have
• Should have a calming feel to make me seem approachable but still professional.
Should not have
• No photos on the card or building plans.

```html
<!DOCTYPE html>
<html lang="en">
<head>
<meta charset="utf-8">
<title>Brackenridge Design Studio – Business Card</title>
<link rel="stylesheet" href="https://fonts.googleapis.com/css2?family=Cinzel:wght@400;600&family=Questrial&display=swap">
<style>
  :root {
    --backdrop: #3a3b3d;
    --paper: #f1f1ef;
    --teal: #2f7a98;
    --slate: #7d7f82;
    --slate-dark: #6a6c6f;
    --ink: #58595b;
    --logo-light: #e6eef2;
  }
  * { box-sizing: border-box; margin: 0; padding: 0; }
  html, body {
    width: 1200px; height: 900px; overflow: hidden;
    background: var(--backdrop);
  }
  .stage {
    width: 1200px; height: 900px;
    display: flex; flex-direction: column;
    align-items: center; justify-content: center; gap: 40px;
  }
  .card {
    position: relative;
    width: 640px; height: 391px;
    overflow: hidden;
    box-shadow: 0 10px 24px rgba(0,0,0,0.35);
  }
  .card__shapes { position: absolute; inset: 0; }

  /* Back side */
  .card--back { background: var(--teal); }
  .card--back .wordmark {
    position: absolute; left: 250px; top: 110px;
    color: var(--logo-light);
  }

  /* Front side */
  .card--front { background: var(--paper); }
  .card--front .wordmark {
    position: absolute; right: 46px; top: 92px;
    color: var(--ink); text-align: right;
  }

  .wordmark {
    font-family: "Cinzel", serif;
    font-weight: 400;
    font-size: 26px;
    line-height: 1.25;
    letter-spacing: 2px;
    text-transform: uppercase;
  }

  .contact {
    position: absolute; left: 46px; top: 96px;
  }
  .contact__name {
    font-family: "Cinzel", serif;
    font-weight: 600;
    font-size: 21px;
    letter-spacing: 1px;
    color: var(--teal);
    text-transform: uppercase;
    margin-bottom: 12px;
  }
  .contact__list {
    list-style: none;
    font-family: "Questrial", sans-serif;
    font-size: 14px;
    line-height: 1.55;
    color: var(--ink);
  }
  .contact__label {
    color: var(--teal);
    font-weight: 700;
    margin-right: 4px;
  }
  .address {
    position: absolute; right: 40px; top: 298px;
    font-family: "Questrial", sans-serif;
    font-style: normal;
    font-size: 14px;
    line-height: 1.4;
    color: var(--ink);
    text-align: right;
  }
</style>
</head>
<body>
<main class="stage">

  <section class="card card--back" aria-label="Business card, back">
    <svg class="card__shapes" viewBox="0 0 640 391" aria-hidden="true">
      <path d="M0,262 Q300,318 640,360 L640,391 L0,391 Z" fill="var(--slate)"/>
      <path d="M0,262 Q300,318 640,360" fill="none" stroke="#ffffff" stroke-width="3"/>
    </svg>
    <div class="wordmark">Brackenridge<br>Design Studio</div>
  </section>

  <section class="card card--front" aria-label="Business card, front">
    <svg class="card__shapes" viewBox="0 0 640 391" aria-hidden="true">
      <polygon points="0,374 392,374 386,391 0,391" fill="var(--slate-dark)"/>
      <polygon points="398,366 640,366 640,391 390,391" fill="var(--teal)"/>
    </svg>

    <div class="contact">
      <h1 class="contact__name">Harriet Oakley</h1>
      <ul class="contact__list">
        <li><span class="contact__label">T:</span>0497 283 541</li>
        <li><span class="contact__label">E:</span>harriet@brackenridgedesignstudio.example.au</li>
        <li><span class="contact__label">W:</span>www.brackenridgedesignstudio.example.au</li>
      </ul>
    </div>

    <div class="wordmark">Brackenridge<br>Design Studio</div>

    <address class="address">
      14 Pembury Road<br>Kilmarra Heights VIC 3187
    </address>
  </section>

</main>
</body>
</html>
```